Brightfield Optics seeks updated contemporary business card

Brightfield Optics utilizes advanced technology and we take pride in the modern look and feel of our practice. We like our current card, but it's been four years so it is time for an update.

Target Market(s)

Females 25-45 make the most health care decisions for their family.

Contact Information for Business Card

Clean front. Back with info and with empty space for appointment time or other small note

Requirements
Must have
• Logo
Ridge Marketvale, 28413 E Larkspur Ave
Cedar Terrace Marketvale, 4638 S Dunmore Rd
Call or text: 509-342-1968
email: hello@brightfieldoptics.example
brightfieldoptics.example
Dr Tobias Werring & Associates

```html
<!DOCTYPE html>
<html lang="en">
<head>
<meta charset="utf-8">
<title>Brightfield Optics — Business Card</title>
<link href="https://fonts.googleapis.com/css2?family=Montserrat:wght@700;800&family=Arimo:wght@400;700&display=swap" rel="stylesheet">
<style>
  :root {
    --navy: #1e2a57;
    --blue: #1f6fb8;
    --blue-light: #2f8fd6;
    --ink: #3a3a3a;
    --grey-text: #6b6b6b;
    --paper: #ffffff;
    --backdrop: #d9d9d7;
  }
  * { box-sizing: border-box; margin: 0; padding: 0; }
  html, body { width: 1200px; height: 801px; overflow: hidden; }
  body {
    background: var(--backdrop);
    font-family: "Arimo", Arial, sans-serif;
    position: relative;
  }
  .card {
    position: absolute;
    top: 246px;
    width: 540px;
    height: 309px;
    box-shadow: 0 6px 18px rgba(0,0,0,0.18);
  }
  /* Appointment side */
  .card--info { left: 40px; background: var(--paper); border-bottom: 3px solid var(--blue); }
  .corner-tab {
    position: absolute; top: 0; right: 0; width: 34px; height: 20px;
    background: linear-gradient(90deg, var(--blue) 0%, #4fa3e0 100%);
  }
  .practice-name {
    position: absolute; left: 30px; top: 30px;
    font-family: "Montserrat", sans-serif; font-weight: 800;
    font-size: 22px; color: var(--navy); letter-spacing: 0.2px;
  }
  .doctor {
    position: absolute; right: 30px; top: 30px; text-align: right;
    font-family: "Montserrat", sans-serif; font-weight: 800;
    font-size: 14px; line-height: 1.15; color: var(--navy);
  }
  .doctor__assoc { display: block; color: var(--blue); font-size: 15px; }
  .form { position: absolute; left: 30px; right: 30px; top: 100px; font-size: 12.5px; color: var(--ink); }
  .form-row { display: flex; align-items: flex-end; gap: 6px; height: 28px; }
  .fill-line { flex: 1; border-bottom: 1px dashed #555; height: 12px; }
  .fill-line--short { flex: 0 0 150px; }
  .days { display: flex; justify-content: space-between; margin-top: 14px; padding-right: 8px; }
  .day { display: flex; align-items: center; gap: 6px; }
  .day__box { width: 12px; height: 12px; border: 1px solid #444; }
  .contact-band {
    position: absolute; left: 0; right: 0; top: 222px; height: 30px;
    background: var(--navy); color: #fff; font-size: 12.5px;
    display: flex; align-items: center; justify-content: space-around; padding: 0 20px;
  }
  .contact-item { display: flex; align-items: center; gap: 6px; }
  .contact-item svg { width: 11px; height: 11px; fill: #fff; }
  .locations {
    position: absolute; left: 30px; right: 30px; top: 266px;
    font-size: 11.5px; color: var(--grey-text); text-align: center;
  }
  /* Name side */
  .card--name {
    left: 620px; background: var(--navy); border-bottom: 3px solid var(--blue);
    display: flex; align-items: center; justify-content: center;
  }
  .card--name .brand {
    font-family: "Montserrat", sans-serif; font-weight: 800;
    font-size: 36px; color: #fff; letter-spacing: 0.5px;
  }
</style>
</head>
<body>
  <section class="card card--info">
    <div class="corner-tab"></div>
    <div class="practice-name">Brightfield Optics</div>
    <div class="doctor">DR TOBIAS WERRING &amp;<span class="doctor__assoc">ASSOCIATES</span></div>

    <div class="form">
      <div class="form-row"><span>Has an appointment on:</span><span class="fill-line"></span></div>
      <div class="form-row"><span>Date :</span><span class="fill-line"></span><span>At</span><span class="fill-line fill-line--short"></span><span>AM/PM</span></div>
      <div class="days">
        <span class="day"><span class="day__box"></span>Mon</span>
        <span class="day"><span class="day__box"></span>Tue</span>
        <span class="day"><span class="day__box"></span>Wed</span>
        <span class="day"><span class="day__box"></span>Thu</span>
        <span class="day"><span class="day__box"></span>Fri</span>
      </div>
    </div>

    <div class="contact-band">
      <span class="contact-item">
        <svg viewBox="0 0 24 24" aria-hidden="true"><path d="M6.6 10.8a15.1 15.1 0 0 0 6.6 6.6l2.2-2.2c.3-.3.7-.4 1-.2 1.1.4 2.3.6 3.6.6.6 0 1 .4 1 1V20c0 .6-.4 1-1 1A17 17 0 0 1 3 4c0-.6.4-1 1-1h3.5c.6 0 1 .4 1 1 0 1.3.2 2.5.6 3.6.1.3 0 .7-.2 1z"/></svg>
        509-342-1968
      </span>
      <span class="contact-item">
        <svg viewBox="0 0 24 24" aria-hidden="true"><path d="M2 5h20v14H2zm2 2v.5l8 5 8-5V7l-8 5z"/></svg>
        hello@brightfieldoptics.example
      </span>
      <span class="contact-item">
        <svg viewBox="0 0 24 24" aria-hidden="true"><circle cx="12" cy="12" r="10"/></svg>
        www.brightfieldoptics.example
      </span>
    </div>

    <div class="locations">Ridge Marketvale, 28413 E Larkspur Ave Cedar Terrace Marketvale, 4638 S Dunmore Rd</div>
  </section>

  <section class="card card--name">
    <div class="brand">Brightfield Optics</div>
  </section>
</body>
</html>
```